ServLoom Website Homepage Design

Please provide your idea of homepage for a hosting company. This project is for DESIGN only, no coding.

It must use/combine colors used in logo, clean, modern look.

Homepage must consist of at least 4 sections (example: testimonials, services, and so on. not necesarily all of them). We would like the navigation to be horizontal, but not mandatory.

You can include a preview of services page (optional, not a must).

Number of Pages Required

1 page

Font styles to use
Sans Serif

```html
<!DOCTYPE html>
<html lang="en">
<head>
<meta charset="utf-8">
<title>ServLoom — Hosting Homepage</title>
<link rel="stylesheet" href="https://fonts.googleapis.com/css2?family=Montserrat:wght@400;600;700;800&family=Open+Sans:wght@400;600;700&display=swap">
<style>
:root{
  --blue:#0a8de0;
  --blue-deep:#0288d9;
  --sky:#b3e0fd;
  --sky-pale:#e0f1fd;
  --card:#f1f8fe;
  --navy:#215d84;
  --yellow:#ffd65a;
  --red:#e3121b;
  --ink:#111;
  --text:#333;
  --muted:#666;
}
*{box-sizing:border-box;margin:0;padding:0}
html,body{width:1200px;height:3793px;overflow:hidden}
body{position:relative;background:#fff;font-family:"Open Sans",Arial,sans-serif;color:var(--text)}
.abs{position:absolute}
.heading{font-family:"Montserrat",Arial,sans-serif;color:var(--ink);font-weight:700}

/* top strip */
.topbar{left:0;top:0;width:1200px;height:35px;background:linear-gradient(90deg,#3aa6ef,#9ed4f8 60%,#e2f2fd)}
.topbar p{position:absolute;right:157px;top:9px;font:700 14px "Open Sans",sans-serif;letter-spacing:1px;color:#555}
.topbar p span{color:var(--blue)}

/* nav */
.nav{left:0;top:35px;width:1200px;height:80px;background:#fff}
.brand{position:absolute;left:155px;top:24px;font:700 29px "Montserrat",sans-serif;color:var(--blue);letter-spacing:1px}
.menu{position:absolute;top:33px;left:0;list-style:none;font:700 15px "Open Sans",sans-serif;color:#222}
.menu li{position:absolute;white-space:nowrap}
.menu .active{color:var(--blue)}
.login{position:absolute;left:947px;top:21px;width:97px;height:41px;background:linear-gradient(90deg,#0a8de0,#35a6ee);color:#fff;font:700 15px "Open Sans",sans-serif;display:flex;align-items:center;justify-content:center}

/* hero */
.hero-bg{left:0;top:115px;width:1200px;height:710px}
.eyebrow{font:700 14px "Open Sans",sans-serif;letter-spacing:3px;color:#555}
.hero-title{left:155px;top:240px;font-size:64px;line-height:72px;font-weight:800}
.btn{display:flex;align-items:center;justify-content:center;font:700 15px "Open Sans",sans-serif;color:#111}
.btn-yellow{background:var(--yellow)}
.btn-white{background:#fff}
.hero-art{left:596px;top:213px;width:435px;height:287px;border-radius:20px;background:radial-gradient(ellipse at center,#d7efff 0%,#a9d9fb 60%,rgba(169,217,251,0) 75%)}

/* domain */
.domain{left:155px;top:674px;width:889px;height:223px;background:var(--sky-pale)}
.domain h3{position:absolute;top:33px;width:100%;text-align:center;font:700 15px "Montserrat",sans-serif;color:#111}
.domain-field{position:absolute;left:85px;top:84px;width:717px;height:55px;background:#fff}
.domain-field .ph{position:absolute;left:14px;top:20px;font-size:11px;color:#999}
.domain-field .sep{position:absolute;left:410px;top:12px;width:2px;height:31px;background:#555}
.domain-field .ext{position:absolute;left:425px;top:19px;font-size:12px;color:#444}
.domain-field .search{position:absolute;left:537px;top:9px;width:168px;height:37px;font-size:11px}
.tlds{position:absolute;top:166px;left:0;width:100%;font-size:12px;color:#222}
.tlds span{position:absolute}
.tlds b{color:var(--red);font-weight:600}

/* section titles */
.sec-title{width:1200px;text-align:center;font-size:46px;left:0}
.sec-sub{width:1200px;text-align:center;font-size:15px;left:0;color:#222}

/* plans */
.band{left:0;top:1384px;width:1200px;height:1151px}
.plan{top:1148px;width:265px;height:545px;background:var(--card)}
.plan h4{position:absolute;top:34px;width:100%;text-align:center;font:700 15px "Open Sans",sans-serif;color:#111}
.plan .price{position:absolute;top:96px;width:100%;text-align:center;font:700 32px "Montserrat",sans-serif;color:#111}
.plan .price small{font:400 16px "Montserrat",sans-serif}
.plan .desc{position:absolute;top:173px;width:100%;text-align:center;font-size:11.5px;line-height:14px;color:#333}
.plan ul{position:absolute;top:239px;left:38px;list-style:none}
.plan li{height:29.4px;font-size:11.5px;color:#222;display:flex;align-items:center;gap:10px}
.plan li svg{flex:none}
.plan .buy{position:absolute;left:46px;top:445px;width:172px;height:53px;border:1.5px solid #222;background:#fff}
.ribbon{left:692px;top:1141px;width:26px;height:121px}

/* features */
.features{left:155px;top:1957px;width:889px;height:447px;background:#fff}
.feat{position:absolute;width:190px}
.feat h5{font:700 15px "Montserrat",sans-serif;color:#111;margin-bottom:18px}
.feat p{font-size:11px;line-height:15.5px;color:#555;padding-left:2px}
.ficon{position:absolute}

/* testimonials */
.testi-bg{left:0;top:2535px;width:1200px;height:711px;background:#eef6fd}
.testi-h{left:150px;top:2770px;font-size:40px;line-height:49px}
.testi-p{left:150px;top:2862px;width:360px;font-size:15px;line-height:21px;color:#222}
.quote-text{left:680px;top:2730px;width:370px;font-size:15px;line-height:20.8px;color:#222}
.avatar{left:680px;top:2918px;width:78px;height:78px;border-radius:50%;background:linear-gradient(160deg,#9a8678,#3c3029)}
.who{left:780px;top:2953px;font:700 15px "Open Sans",sans-serif;color:#111;letter-spacing:.5px}
.dot{top:3022px;width:13px;height:13px;border-radius:50%;background:#c9ced3}

/* footer */
.foot-bg{left:0;top:3246px;width:1200px;height:547px;background:linear-gradient(180deg,#b4def9,#5aaaee 55%,#3d96e3)}
.cta{left:150px;top:3170px;width:900px;height:165px;background:var(--navy)}
.cta h3{position:absolute;left:66px;top:50px;font:700 24px "Montserrat",sans-serif;color:#fff}
.cta p{position:absolute;left:66px;top:86px;width:250px;font-size:11px;line-height:13px;color:#dce9f3}
.cta .email{position:absolute;left:370px;top:56px;width:453px;height:53px;background:#fff}
.cta .email span{position:absolute;left:29px;top:19px;font-size:12px;color:#888}
.cta .sub{position:absolute;left:281px;top:0;width:172px;height:53px;font-size:16px}
.foot-h{font:700 15px "Montserrat",sans-serif;color:#111}
.follow{left:150px;top:3428px;font-size:22px}
.social{top:3506px;display:flex;align-items:center;gap:6px;font:600 11px "Open Sans",sans-serif;color:#111}
.social i{display:block;width:14px;height:14px;background:#111;border-radius:3px}
.fcol{top:3431px;list-style:none}
.fcol li{font-size:15px;color:#111;height:41px}
.fcol li.t{font:700 15px "Montserrat",sans-serif;height:48px}
.legal{top:3730px;font-size:11px;color:#111}
</style>
</head>
<body>

<div class="abs topbar"><p>START 7 DAY <span>FREE TRIAL</span></p></div>

<header class="abs nav">
  <div class="brand">ServLoom</div>
  <ul class="menu">
    <li class="active" style="left:405px">HOME</li>
    <li style="left:489px">DOMAIN</li>
    <li style="left:592px">HOSTING</li>
    <li style="left:704px">SERVICES</li>
    <li style="left:810px">CONTACT</li>
  </ul>
  <a class="login">LOGIN</a>
</header>

<svg class="abs hero-bg" width="1200" height="710" viewBox="0 0 1200 710" aria-hidden="true">
  <defs>
    <linearGradient id="heroGrad" x1="0" x2="1" y1="0" y2="0">
      <stop offset="0" stop-color="#4fb1ef"/>
      <stop offset=".35" stop-color="#b3e0fd"/>
      <stop offset="1" stop-color="#bfe4fd"/>
    </linearGradient>
  </defs>
  <polygon points="0,0 1200,0 1200,467 0,705" fill="url(#heroGrad)"/>
</svg>

<p class="abs eyebrow" style="left:155px;top:220px">WE PROVIDE</p>
<h1 class="abs heading hero-title">Best Hosting<br>Solution</h1>
<a class="abs btn btn-yellow" style="left:155px;top:458px;width:172px;height:53px">GET STARTED</a>
<a class="abs btn btn-white" style="left:355px;top:458px;width:172px;height:53px">MORE DETAILS</a>
<div class="abs hero-art" role="img" aria-label="Isometric illustration of server racks, cloud, laptop and devices linked by network lines"></div>

<section class="abs domain">
  <h3>Do You Want Your Premium Domain?</h3>
  <div class="domain-field">
    <span class="ph">Type Your Domain Address</span>
    <span class="sep"></span>
    <span class="ext">.info &#9662;</span>
    <a class="btn btn-yellow search">SEARCH DOMAIN</a>
  </div>
  <div class="tlds">
    <span style="left:87px"><b>.net</b>&nbsp; $14.99</span>
    <span style="left:240px"><b>.com</b>&nbsp; $14.99</span>
    <span style="left:400px"><b>.info</b>&nbsp; $14.99</span>
    <span style="left:555px"><b>.store</b>&nbsp; $14.99</span>
    <span style="left:718px"><b>.co</b>&nbsp; $14.99</span>
  </div>
</section>

<svg class="abs band" width="1200" height="1151" viewBox="0 0 1200 1151" aria-hidden="true">
  <defs>
    <linearGradient id="bandGrad" x1="0" x2="1" y1="0" y2="0">
      <stop offset="0" stop-color="#b3e0fd"/>
      <stop offset=".45" stop-color="#5fb5ee"/>
      <stop offset="1" stop-color="#0288d9"/>
    </linearGradient>
  </defs>
  <polygon points="0,0 1200,324 1200,1151 0,1151" fill="url(#bandGrad)"/>
</svg>

<h2 class="abs heading sec-title" style="top:985px">Best Hosting Plans</h2>
<p class="abs sec-sub" style="top:1043px">Lorem ipsum dolor sit amet, consectetur adipiscing elit.</p>

<svg width="0" height="0" style="position:absolute">
  <symbol id="tick" viewBox="0 0 14 14"><circle cx="7" cy="7" r="7" fill="#e3121b"/><path d="M3.8 7.2l2.2 2.2 4.2-4.5" fill="none" stroke="#fff" stroke-width="1.8"/></symbol>
</svg>

<div class="abs plan" style="left:155px">
  <h4>PRICE 1</h4>
  <div class="price">%25/<small>Month</small></div>
  <p class="desc">Lorem ipsum dolor sit amet,<br>consectetur adipiscing elit.</p>
  <ul>
    <li><svg width="14" height="14"><use href="#tick"/></svg>Lorem ipsum dolor sit amet,</li>
    <li><svg width="14" height="14"><use href="#tick"/></svg>Lorem ipsum dolor sit amet,</li>
    <li><svg width="14" height="14"><use href="#tick"/></svg>Lorem ipsum dolor sit amet,</li>
    <li><svg width="14" height="14"><use href="#tick"/></svg>Lorem ipsum dolor sit amet,</li>
    <li><svg width="14" height="14"><use href="#tick"/></svg>Lorem ipsum dolor sit amet,</li>
    <li><svg width="14" height="14"><use href="#tick"/></svg>Lorem ipsum dolor sit amet,</li>
  </ul>
  <a class="btn buy">BUY NOW</a>
</div>
<div class="abs plan" style="left:467px">
  <h4>PRICE 2</h4>
  <div class="price">%75/<small>Month</small></div>
  <p class="desc">Lorem ipsum dolor sit amet,<br>consectetur adipiscing elit.</p>
  <ul>
    <li><svg width="14" height="14"><use href="#tick"/></svg>Lorem ipsum dolor sit amet,</li>
    <li><svg width="14" height="14"><use href="#tick"/></svg>Lorem ipsum dolor sit amet,</li>
    <li><svg width="14" height="14"><use href="#tick"/></svg>Lorem ipsum dolor sit amet,</li>
    <li><svg width="14" height="14"><use href="#tick"/></svg>Lorem ipsum dolor sit amet,</li>
    <li><svg width="14" height="14"><use href="#tick"/></svg>Lorem ipsum dolor sit amet,</li>
    <li><svg width="14" height="14"><use href="#tick"/></svg>Lorem ipsum dolor sit amet,</li>
  </ul>
  <a class="btn buy">BUY NOW</a>
</div>
<div class="abs plan" style="left:777px">
  <h4>PRICE 3</h4>
  <div class="price">%125/<small>Month</small></div>
  <p class="desc">Lorem ipsum dolor sit amet,<br>consectetur adipiscing elit.</p>
  <ul>
    <li><svg width="14" height="14"><use href="#tick"/></svg>Lorem ipsum dolor sit amet,</li>
    <li><svg width="14" height="14"><use href="#tick"/></svg>Lorem ipsum dolor sit amet,</li>
    <li><svg width="14" height="14"><use href="#tick"/></svg>Lorem ipsum dolor sit amet,</li>
    <li><svg width="14" height="14"><use href="#tick"/></svg>Lorem ipsum dolor sit amet,</li>
    <li><svg width="14" height="14"><use href="#tick"/></svg>Lorem ipsum dolor sit amet,</li>
    <li><svg width="14" height="14"><use href="#tick"/></svg>Lorem ipsum dolor sit amet,</li>
  </ul>
  <a class="btn buy">BUY NOW</a>
</div>

<svg class="abs ribbon" width="26" height="121" viewBox="0 0 26 121">
  <polygon points="0,0 26,0 26,121 13,106 0,121" fill="#e3121b"/>
  <text x="17" y="76" transform="rotate(-90 17 76)" font-family="Montserrat,sans-serif" font-weight="700" font-size="10" fill="#fff">POPULAR</text>
</svg>

<h2 class="abs heading sec-title" style="top:1792px">The Best Feature You Will Love</h2>
<p class="abs sec-sub" style="top:1849px">Lorem ipsum dolor sit amet, consectetur adipiscing elit.</p>

<section class="abs features">
  <svg class="ficon" style="left:58px;top:55px" width="44" height="44" viewBox="0 0 44 44" fill="none" stroke="#222" stroke-width="1.6">
    <rect x="1" y="1" width="42" height="42" rx="2"/><path d="M1 9h42"/><path d="M6 5h18M30 5h2M35 5h2M39 5h2"/>
    <rect x="7" y="18" width="5" height="5"/><rect x="7" y="30" width="5" height="5"/>
    <text x="15" y="23" font-size="8" font-family="Open Sans,sans-serif" font-weight="700" fill="#222" stroke="none">.com</text>
    <text x="15" y="35" font-size="8" font-family="Open Sans,sans-serif" font-weight="700" fill="#222" stroke="none">.net</text>
  </svg>
  <div class="feat" style="left:126px;top:60px"><h5>Unlimited Domain</h5><p>Lorem Ipsum Dolor Sit Amet,<br>Consectetur Adipiscing Elit.<br>Nulla Imperdiet Faucibus<br>Varius Gravida Amet Mi<br>Cursus Mollis.</p></div>

  <svg class="ficon" style="left:335px;top:55px" width="46" height="38" viewBox="0 0 46 38" fill="none" stroke="#222" stroke-width="1.6">
    <rect x="1" y="1" width="44" height="36" rx="2"/><path d="M1 8h44M5 4.5h2M9 4.5h2M13 4.5h2"/>
    <path d="M7 33V22h5v11M15 33V16h5v17M23 33V25h5v8M31 33V19h5v14M5 33h36"/>
  </svg>
  <div class="feat" style="left:407px;top:50px"><h5>Analystics</h5><p>Lorem Ipsum Dolor Sit Amet,<br>Consectetur Adipiscing Elit.<br>Nulla Imperdiet Faucibus<br>Varius Gravida Amet Mi<br>Cursus Mollis.</p></div>

  <svg class="ficon" style="left:611px;top:55px" width="44" height="44" viewBox="0 0 44 44" fill="none" stroke="#222" stroke-width="1.6">
    <path d="M1 18l21-14 21 14v24H1z"/><path d="M1 18l21 14 21-14"/><rect x="9" y="8" width="26" height="18" fill="#fff"/>
    <path d="M13 13h18M13 17h18M13 21h12"/>
  </svg>
  <div class="feat" style="left:681px;top:50px"><h5>Free Mail</h5><p>Lorem Ipsum Dolor Sit Amet,<br>Consectetur Adipiscing Elit.<br>Nulla Imperdiet Faucibus<br>Varius Gravida Amet Mi<br>Cursus Mollis.</p></div>

  <svg class="ficon" style="left:67px;top:254px" width="38" height="44" viewBox="0 0 38 44" fill="none" stroke="#222" stroke-width="2.4">
    <path d="M19 2L2 8v12c0 11 8 19 17 22 9-3 17-11 17-22V8z"/><path d="M11 22l6 6 11-12"/>
  </svg>
  <div class="feat" style="left:126px;top:255px"><h5>Reliable Data Centers</h5><p>Lorem Ipsum Dolor Sit Amet,<br>Consectetur Adipiscing Elit.<br>Nulla Imperdiet Faucibus<br>Varius Gravida Amet Mi<br>Cursus Mollis.</p></div>

  <svg class="ficon" style="left:343px;top:254px" width="34" height="46" viewBox="0 0 34 46" fill="none" stroke="#222" stroke-width="1.8">
    <path d="M17 44S2 27 2 16a15 15 0 0 1 30 0c0 11-15 28-15 28z"/><circle cx="17" cy="16" r="6"/>
  </svg>
  <div class="feat" style="left:410px;top:255px"><h5>Multiple Locations</h5><p>Lorem Ipsum Dolor Sit Amet,<br>Consectetur Adipiscing Elit.<br>Nulla Imperdiet Faucibus<br>Varius Gravida Amet Mi<br>Cursus Mollis.</p></div>

  <svg class="ficon" style="left:612px;top:254px" width="44" height="44" viewBox="0 0 44 44" fill="none" stroke="#222" stroke-width="1.6">
    <circle cx="22" cy="22" r="20"/><ellipse cx="22" cy="22" rx="9" ry="20"/><path d="M2 22h40M6 11h32M6 33h32M22 2v40"/>
    <circle cx="22" cy="22" r="6" fill="#fff"/>
  </svg>
  <div class="feat" style="left:681px;top:255px"><h5>Global Network</h5><p>Lorem Ipsum Dolor Sit Amet,<br>Consectetur Adipiscing Elit.<br>Nulla Imperdiet Faucibus<br>Varius Gravida Amet Mi<br>Cursus Mollis.</p></div>
</section>

<div class="abs testi-bg"></div>
<svg class="abs" style="left:0;top:2535px" width="1200" height="711" viewBox="0 0 1200 711" aria-hidden="true">
  <polygon points="0,0 440,0 0,440" fill="#f6fbff"/>
  <polygon points="0,470 260,260 680,711 0,711" fill="#f4f9fe"/>
</svg>

<p class="abs eyebrow" style="left:150px;top:2738px;font-size:11px;color:#333">CLIENT FEEDBACK</p>
<h2 class="abs heading testi-h">What People Say<br>About Us?</h2>
<p class="abs testi-p">Lorem ipsum dolor sit amet, consectetur adipiscing elit. Purus in cursus dolor amet, quis.</p>

<svg class="abs" style="left:680px;top:2643px" width="54" height="41" viewBox="0 0 54 41">
  <path d="M0 41V20L9 0h12l-6 17h8v24zM31 41V20L40 0h12l-6 17h8v24z" fill="#1585d8"/>
</svg>
<p class="abs quote-text">Lorem ipsum dolor sit amet, consectetur adipiscing elit. Mauris convallis malesuada pretium ac urna. A senectus sed est sem quam tortor tempus. Diam, viverra mi dictumst sed. Venenatis et nibh a sagittis. In sed tortor et maecenas id commodo ut. Condimentum eget ullamcorper elit, cras sed scelerisque ipsum. Tincidunt magna eu adipiscing egestas vulputate maecenas pretium.</p>
<div class="abs avatar" role="img" aria-label="Client portrait photo"></div>
<p class="abs who">MARLEN ODARI</p>
<span class="abs dot" style="left:680px;background:#2f9ae6"></span>
<span class="abs dot" style="left:707px"></span>
<span class="abs dot" style="left:734px"></span>
<span class="abs dot" style="left:761px"></span>
<span class="abs dot" style="left:788px;background:#dde1e5"></span>
<span class="abs dot" style="left:815px;background:#e6e9ec"></span>

<div class="abs foot-bg"></div>

<section class="abs cta">
  <h3>Want To Get Started?</h3>
  <p>Lorem ipsum dolor sit amet, consectetur adipiscing elit.</p>
  <div class="email"><span>Your Email Address</span><a class="btn btn-yellow sub">SUBSCRIBE</a></div>
</section>

<h3 class="abs foot-h follow">Follow Us</h3>
<span class="abs social" style="left:158px"><i></i>Circlebook</span>
<span class="abs social" style="left:158px;top:3532px"><i></i>Chirpline</span>
<span class="abs social" style="left:262px"><i style="border-radius:50%"></i>Snapgrid</span>

<ul class="abs fcol" style="left:518px"><li class="t">FEATURES</li><li>Lorem</li><li>Lorem</li><li>Lorem</li><li>Lorem</li></ul>
<ul class="abs fcol" style="left:735px"><li class="t">SERVICES</li><li>Lorem</li><li>Lorem</li><li>Lorem</li><li>Lorem</li></ul>
<ul class="abs fcol" style="left:951px"><li class="t">LINKS</li><li>Lorem</li><li>Lorem</li><li>Lorem</li><li>Lorem</li></ul>

<p class="abs legal" style="left:150px">Copyright ServLoom Company 2021 - Legal</p>
<p class="abs legal" style="left:779px">Terms And Conditions</p>
<p class="abs legal" style="left:958px">Privacy Policy</p>

</body>
</html>
```